Stainless Steel Water Bottle Packaging

We need a design for our cylindrical water bottle packaging.

Please see attached template (500ml cola bottle template .ai file) for exact dimensions.

VORO is defined as the elemental forces of nature embodied in an object or person. The design should be eye catching and draw potential clients in. Although its a cylindrical bottle/box, the front which would face the customer when sitting on a shelf should clearly display our logo.

Industry/Entity Type

Steel

Requirements
Must have
• Designed to the specifications of the attached template (see attached)
• Our VORO Logo (see attached) and website www.vorobottle.example(in smaller font) must appear.
• Size of bottle must appear - '17 oz/500 ml'
• These should appear somewhere:
• 'INULATED DOUBLE-WALL STAINLESS STEEL WATER BOTTLE'
• 'VORO Bottles magically keeps drinks cold for up to 24hrs, hot for 12',
• 'BPA Free'
• 'For every VORO bottle purchased, a portion of proceeds will go towards charity. Each of our colour's have been assigned a specific charity. Please visit www.vorobottle.example to find out which charity you helped support!'
• The Top circle - just our Symbol (flame/drop)
• The bottom circle - 'Inc. Designed in Canada made in China' on the outer edge leaving the middle empty for the UPC code.
• Reference website for the bottle case I'm looking for:
• http://shopkorinday.example/t-flow-lagoon-pink-insulated-water-bottle
Nice to have
• illustration of our water bottle shape (see attached) appearing somewhere on the box is something i had in mind but definitely not necessary.

```html
<!DOCTYPE html>
<html lang="en">
<head>
<meta charset="utf-8">
<title>VORO Bottle Packaging</title>
<link rel="stylesheet" href="https://fonts.googleapis.com/css2?family=Montserrat:wght@400;500;600;700;800&display=swap">
<style>
  :root {
    --bg: #111111;
    --cream: #fdf8ea;
    --orange: #f6a81c;
    --orange-light: #f9c64e;
    --blue: #1e9cd4;
    --blue-light: #6cc3e6;
    --teal: #1a8fb8;
    --navy: #14306a;
    --ink: #333333;
    --green: #3e9a3a;
    --cold: #1f5fa8;
    --hot: #e9741c;
  }
  * { box-sizing: border-box; margin: 0; padding: 0; }
  html, body { width: 1200px; height: 880px; overflow: hidden; }
  body {
    background: var(--bg);
    font-family: "Montserrat", sans-serif;
    position: relative;
  }

  /* Wrap label */
  .wrap-label {
    position: absolute;
    left: 40px; top: 40px;
    width: 708px; height: 800px;
    background: var(--cream);
    overflow: hidden;
  }
  .wash {
    position: absolute;
    top: 0; bottom: 0;
  }
  .wash--warm {
    left: 0; width: 300px;
    background: linear-gradient(90deg, var(--orange) 0%, var(--orange-light) 70%, rgba(249,198,78,0) 100%);
  }
  .wash--cool {
    left: 400px; width: 276px;
    background: linear-gradient(90deg, rgba(108,195,230,0) 0%, var(--blue-light) 25%, var(--blue) 75%, var(--teal) 100%);
  }
  .title-band {
    position: absolute;
    right: 0; top: 0; bottom: 0;
    width: 32px;
    background: var(--navy);
    display: flex; align-items: center; justify-content: center;
  }
  .title-band__text {
    writing-mode: vertical-rl;
    transform: rotate(180deg);
    color: #ffffff;
    font-weight: 800;
    font-size: 15.5px;
    letter-spacing: 0.3px;
    white-space: nowrap;
  }

  .brand {
    position: absolute;
    left: 0; width: 676px;
    top: 52px;
    text-align: center;
  }
  .brand__name {
    display: inline-flex; align-items: center; gap: 10px;
    color: var(--teal);
    font-weight: 500;
    font-size: 44px;
    letter-spacing: 6px;
    line-height: 1;
  }
  .brand__dot {
    width: 14px; height: 14px;
    border-radius: 50%;
    background: var(--orange);
  }
  .brand__url {
    margin-top: 10px;
    font-size: 13px;
    letter-spacing: 1.4px;
    color: var(--ink);
    font-weight: 500;
  }

  .claims {
    position: absolute;
    left: 42px; top: 270px;
    width: 150px;
    color: var(--ink);
  }
  .claims__badge {
    width: 78px; height: 78px;
    border-radius: 50%;
    background: #ffffff;
    border: 3px solid var(--green);
  }
  .claims__lead {
    margin-top: 14px;
    font-size: 13px;
    font-weight: 500;
    letter-spacing: 0.6px;
    line-height: 1.3;
  }
  .temps {
    display: flex; gap: 10px;
    margin-top: 12px;
  }
  .temp {
    width: 60px; height: 60px;
    border-radius: 50%;
    color: #ffffff;
    font-weight: 700;
    font-size: 13px;
    line-height: 1.1;
    display: flex; flex-direction: column; align-items: center; justify-content: center;
    border: 2px solid rgba(255,255,255,0.6);
  }
  .temp--cold { background: var(--cold); }
  .temp--hot { background: var(--hot); }
  .temp__time { font-weight: 500; }
  .claims__copy {
    margin-top: 20px;
    font-size: 11.5px;
    line-height: 1.3;
  }
  .claims__copy p + p { margin-top: 12px; }
  .claims__copy strong { font-weight: 700; }

  .bottle-art {
    position: absolute;
    left: 288px; top: 218px;
    width: 108px; height: 520px;
    border-radius: 40px 40px 24px 24px;
    background: linear-gradient(90deg, #e6e0d4, #fbf8f1 45%, #ddd6c8);
  }
  .size {
    position: absolute;
    left: 290px; top: 748px;
    font-size: 13px;
    font-weight: 500;
    color: var(--ink);
  }

  /* Lid circles */
  .lid {
    position: absolute;
    left: 780px;
    width: 380px; height: 380px;
    border-radius: 50%;
    background: var(--cream);
  }
  .lid--top { top: 40px; display: flex; align-items: center; justify-content: center; }
  .lid--bottom { top: 460px; }
  .lid__name {
    color: var(--teal);
    font-weight: 500;
    font-size: 56px;
    letter-spacing: 8px;
  }
  .lid__ring { width: 380px; height: 380px; display: block; }
  .lid__ring text {
    font-family: "Montserrat", sans-serif;
    font-size: 17px;
    font-weight: 500;
    fill: var(--ink);
    letter-spacing: 1px;
  }
</style>
</head>
<body>
  <section class="wrap-label">
    <div class="wash wash--warm" role="img" aria-label="Orange watercolour splash"></div>
    <div class="wash wash--cool" role="img" aria-label="Blue watercolour splash"></div>

    <header class="brand">
      <div class="brand__name"><span class="brand__dot"></span>VORO</div>
      <div class="brand__url">www.vorobottle.example</div>
    </header>

    <div class="claims">
      <div class="claims__badge"></div>
      <p class="claims__lead">VORO Bottles<br>Magically<br>Keeps Drinks</p>
      <div class="temps">
        <div class="temp temp--cold"><span>COLD</span><span class="temp__time">24hrs</span></div>
        <div class="temp temp--hot"><span>HOT</span><span class="temp__time">12hrs</span></div>
      </div>
      <div class="claims__copy">
        <p>For every VORO bottle purchased, a portion of proceeds will go towards charity. Each of our colour's have been assigned a specific charity.</p>
        <p>Please visit <strong>www.vorobottle.example</strong> to find out which charity you helped support!</p>
      </div>
    </div>

    <div class="bottle-art" role="img" aria-label="Outline illustration of the insulated water bottle"></div>
    <div class="size">17 oz/500 ml</div>

    <div class="title-band">
      <span class="title-band__text">INULATED DOUBLE-WALL STAINLESS STEEL WATER BOTTLE</span>
    </div>
  </section>

  <div class="lid lid--top">
    <span class="lid__name">VORO</span>
  </div>

  <div class="lid lid--bottom">
    <svg class="lid__ring" viewBox="0 0 380 380" aria-label="Inc. Designed in Canada made in China">
      <defs>
        <path id="arc-top" d="M 40 190 A 150 150 0 0 1 340 190"/>
        <path id="arc-bottom" d="M 28 190 A 162 162 0 0 0 352 190"/>
      </defs>
      <text><textPath href="#arc-top" startOffset="50%" text-anchor="middle">Inc. Designed in Canada made in China</textPath></text>
      <text><textPath href="#arc-bottom" startOffset="50%" text-anchor="middle">Inc. Designed in Canada made in China</textPath></text>
    </svg>
  </div>
</body>
</html>
```